Brell Harbor Company Business Cards

Front and Back Business Card - logo and text setup - cool design. I need workable photoshop or illustrator files so I can setup each employee card with design that is created
Updates

Hi everyone, thank you for the great entries. Please no more white and blue cards - there are so many already - black and silver only now please. thanks!

Target Market(s)

Construction Industry - Facility Managers

Industry/Entity Type

Construction

Contact Information for Business Card

I really like contemporary simplistic looks - clean neat....not opposed to seeing some black backrounds

Requirements
Must have
• Logo/website address with design on front only - www.brellharbor-example.com (logo attached)
• Back:
• Name/Title/Company Address/Phone/email address
Nice to have
• Cool design
Should not have
• Nothing gimmicky like Fire or Water - since we are a Fire Protection company - it has all been done

```html
<!DOCTYPE html>
<html lang="en">
<head>
<meta charset="utf-8">
<title>Brell Harbor Company Business Cards</title>
<link href="https://fonts.googleapis.com/css2?family=Lato:wght@400;700;900&display=swap" rel="stylesheet">
<style>
  :root {
    --backdrop: #e9e4dc;
    --kraft-light: #d8b98e;
    --kraft-mid: #c9a474;
    --kraft-dark: #b68c5d;
    --ink: #17110a;
    --rule: #6e5a40;
    --card-shadow: rgba(40, 25, 10, 0.35);
  }
  * { margin: 0; padding: 0; box-sizing: border-box; }
  html, body {
    width: 1200px;
    height: 900px;
    overflow: hidden;
  }
  body {
    background: var(--backdrop);
    font-family: "Lato", sans-serif;
    color: var(--ink);
    position: relative;
  }
  .card {
    position: absolute;
    width: 556px;
    height: 343px;
    background: radial-gradient(ellipse at 40% 10%, var(--kraft-light) 0%, var(--kraft-mid) 55%, var(--kraft-dark) 100%);
    box-shadow: 3px 4px 8px var(--card-shadow);
  }
  .card-back { left: 330px; top: 90px; }
  .card-front { left: 330px; top: 470px; }

  .contact {
    position: absolute;
    left: 0; right: 0; top: 78px;
    text-align: center;
  }
  .contact-name {
    font-weight: 700;
    font-size: 20px;
    letter-spacing: 0.3px;
    line-height: 22px;
  }
  .contact-title {
    font-size: 16px;
    line-height: 19px;
  }
  .rule {
    width: 196px;
    height: 1px;
    background: var(--rule);
    margin: 0 auto;
  }
  .rule-top { margin-top: 10px; margin-bottom: 10px; }
  .rule-bottom { margin-top: 10px; margin-bottom: 14px; }
  .contact-lines p,
  .contact-address p {
    font-size: 16px;
    line-height: 20px;
  }
  .contact-lines strong { font-weight: 700; }

  .brand-name {
    position: absolute;
    left: 0; right: 0; top: 122px;
    text-align: center;
    font-weight: 900;
    font-size: 54px;
    letter-spacing: -0.5px;
    line-height: 60px;
  }
  .brand-url {
    position: absolute;
    left: 0; right: 0; top: 284px;
    text-align: center;
    font-size: 16px;
  }
</style>
</head>
<body>
  <section class="card card-back" aria-label="Business card back">
    <div class="contact">
      <p class="contact-name">MARCUS ELLERY</p>
      <p class="contact-title">Managing Director</p>
      <div class="rule rule-top"></div>
      <div class="contact-lines">
        <p><strong>P:</strong> 044-555 010 200</p>
        <p><strong>E:</strong> info@brellharbor-example.com</p>
        <p><strong>W:</strong> www.brellharbor-example.com</p>
      </div>
      <div class="rule rule-bottom"></div>
      <div class="contact-address">
        <p>12345, Address Goes Here</p>
        <p>Country Name, 123456.</p>
      </div>
    </div>
  </section>

  <section class="card card-front" aria-label="Business card front">
    <p class="brand-name">Brell Harbor</p>
    <p class="brand-url">www.brellharbor-example.com</p>
  </section>
</body>
</html>
```